Brimvane.com fiber optic internet website redesign

We need a new website design for our fiber optic internet company that provides internet, phone, and tv services. It should use the text "Marrowfen fiber optics", and "I beamed up with Marrowfen". The design should use the color blue and the attached logo.
We are a 30 year old internet company who started as a dial up internet provider in our basement. Today we design, build, and maintain our own fiber optic internet network to provide service to residential, business, educational, healthcare, and governmental customers

```html
<!DOCTYPE html>
<html lang="en">
<head>
<meta charset="utf-8">
<title>Brimvane.com – Marrowfen Fiber Optics</title>
<link href="https://fonts.googleapis.com/css2?family=Poppins:wght@400;500;600&family=Roboto:wght@400;500;700&family=Roboto+Condensed:wght@700&display=swap" rel="stylesheet">
<style>
:root{
  --blue:#0a4aa8;
  --blue-deep:#0b3e8e;
  --red:#d7141a;
  --ink:#111;
  --text:#555;
  --pale:#eaf3fc;
  --dark:#1b1b1b;
  --white:#fff;
  --line-soft:#bcd4f5;
}
*{box-sizing:border-box;margin:0;padding:0}
html,body{width:1200px;height:3995px;overflow:hidden}
body{position:relative;font-family:Roboto,Arial,sans-serif;color:var(--text);background:var(--white)}
.abs{position:absolute}
a{color:inherit;text-decoration:none}
.heading{font-family:Poppins,Arial,sans-serif;font-weight:500;color:var(--ink)}
.heading .accent{color:var(--red);font-weight:400}
.btn{position:absolute;display:flex;align-items:center;justify-content:center;gap:8px;border-radius:24px;font-weight:700;font-size:14px;color:var(--white);background:var(--blue)}
.btn svg{width:13px;height:13px}
.rule{position:absolute;height:2px;background:var(--blue)}
.band-edge{position:absolute;left:0;width:1200px;height:3px}

/* header */
.site-header{top:0;left:0;width:1200px;height:102px;background:var(--white)}
.brand{display:flex;align-items:center;gap:12px}
.brand-dot{width:56px;height:56px;border-radius:50%;background:var(--blue)}
.brand-name{font-family:Roboto,Arial,sans-serif;font-weight:500;font-size:34px;color:#222;line-height:1}
.brand-sub{font-size:14px;color:#222;margin-top:2px;padding-left:24px}
.top-links{left:628px;top:0;width:210px;height:34px;background:var(--blue);color:var(--white);font-size:14px;font-weight:700;display:flex;align-items:center;justify-content:center;gap:10px;clip-path:polygon(0 0,100% 0,100% 100%,6% 100%)}
.top-phone{left:832px;top:0;width:254px;height:34px;background:var(--red);color:var(--white);font-size:19px;font-weight:700;display:flex;align-items:center;justify-content:center;gap:10px;clip-path:polygon(0 0,100% 0,95% 100%,5% 100%)}
.top-line{left:1086px;top:0;width:114px;height:3px;background:var(--red)}
.main-nav{left:543px;top:62px;display:flex;font-size:13px;font-weight:700;color:#111}
.main-nav span{padding:0 8px;border-right:1px solid #333;line-height:12px}
.main-nav span:first-child{padding-left:0;color:var(--red)}
.main-nav span:last-child{border:0;padding-right:0}

/* hero */
.hero{top:102px;left:0;width:1200px;height:476px;background:linear-gradient(90deg,#1f2a36 0%,#3a4450 45%,#6b737c 70%,#9ea4aa 100%)}
.hero-title{left:108px;top:202px;font-family:Poppins,Arial,sans-serif;font-weight:600;font-size:46px;color:var(--white)}
.hero-sub{left:112px;top:280px;width:470px;font-size:19px;font-weight:700;line-height:32px;color:var(--white);text-transform:uppercase}
.hero-cta{left:113px;top:404px;width:163px;height:44px;border:2px solid var(--white)}
.hero-badge{left:866px;top:310px;width:312px;height:50px;background:var(--red);border-radius:6px;color:var(--white);font-weight:700;font-size:18px;display:flex;align-items:center;gap:10px;padding-left:8px;white-space:nowrap}
.hero-badge i{width:30px;height:30px;border-radius:50%;background:var(--white);display:block;flex:none}

/* about */
.photo-circle{border-radius:50%}
.about-title{left:616px;top:692px;font-size:46px}
.about-copy{left:616px;top:778px;width:470px;font-size:14px;line-height:26px}
.about-copy p+p{margin-top:16px}

/* pricing */
.pricing-band{top:1187px;left:0;width:1200px;height:418px;background:var(--pale)}
.section-title{width:1200px;left:0;text-align:center;font-size:46px}
.price-card{top:1356px;width:260px;height:326px;border-radius:6px;color:var(--white);text-align:center;padding-top:26px}
.price-card .name{font-size:16px;font-weight:700;line-height:29px}
.price-card .bar{width:50px;height:2px;background:var(--white);margin:8px auto 14px}
.price-card .amount{font-family:"Roboto Condensed",Roboto,Arial,sans-serif;font-weight:700;font-size:50px;line-height:54px;letter-spacing:-1px}
.price-card .amount small{font-size:16px}
.price-card .desc{font-size:14px;line-height:23px;padding:14px 26px 0}
.card-dark{background:linear-gradient(160deg,#2b2b2b,#161616)}
.card-blue{background:linear-gradient(160deg,#0d48b0,#06266a)}
.card-red{background:linear-gradient(160deg,#c3151a,#6b0508)}
.buy{top:1660px;width:160px;height:43px;background:var(--red);border:2px solid var(--white);box-shadow:0 3px 8px rgba(0,0,0,.2)}

/* services */
.service{display:flex;gap:14px}
.service-icon{width:76px;height:76px;border-radius:50%;border:4px solid var(--white);box-shadow:0 4px 12px rgba(0,0,0,.25);display:flex;align-items:center;justify-content:center;flex:none}
.service-icon.blue{background:var(--blue)}
.service-icon.red{background:var(--red)}
.service-icon svg{width:40px;height:40px}
.service h3{font-size:16px;font-weight:500;color:#111;margin:8px 0 10px}
.service p{font-size:13px;line-height:24px;color:#333;width:300px}

/* experience */
.experience{top:2530px;left:0;width:1200px;height:490px;background:linear-gradient(180deg,#0a4fb6,#0a44a0)}
.exp-title{left:0;width:1200px;text-align:center;top:2590px;font-family:Poppins,Arial,sans-serif;font-size:46px;font-weight:400;color:var(--white)}
.exp-title b{font-weight:600}
.exp-copy{left:150px;width:900px;top:2686px;text-align:center;color:var(--white);font-size:14px;line-height:26px}
.feature{width:260px;text-align:center;color:var(--white);font-weight:700;font-size:18px}
.feature svg{width:90px;height:90px;display:block;margin:0 auto 12px}

/* service area */
.map{top:3020px;left:0;width:1200px;height:625px;background:linear-gradient(135deg,#e8f0ea,#f1f4f1 50%,#e6ede8)}
.area-card{left:573px;top:3101px;width:513px;height:452px;background:var(--white);box-shadow:0 4px 18px rgba(0,0,0,.12);border-radius:4px}
.area-title{left:616px;top:3125px;font-size:46px}
.area-list{left:616px;top:3222px;width:400px;font-size:14px;line-height:26px}
.area-list .first{color:var(--blue)}
.call-label{left:616px;top:3371px;font-size:18px;color:var(--blue)}
.call-nums{left:616px;top:3402px;font-size:29px;font-weight:700;color:#111}

/* footer */
.site-footer{top:3645px;left:0;width:1200px;height:350px;background:var(--dark);color:var(--white)}
.footer-nav{left:526px;top:3706px;display:flex;font-size:13px;font-weight:700}
.footer-nav span{padding:0 8px;border-right:1px solid #ccc;line-height:12px}
.footer-nav span:first-child{padding-left:0}
.footer-nav span:last-child{border:0}
.footer-col{top:3780px;font-size:14px;line-height:30px}
.footer-col h4{font-size:17px;font-weight:700;margin-bottom:2px}
.footer-rule{left:248px;top:3923px;width:704px;height:1px;background:#555}
.copyright{left:0;width:1200px;text-align:center;top:3938px;font-size:13px}
</style>
</head>
<body>

<!-- header -->
<header class="site-header abs">
  <div class="brand abs" style="left:110px;top:20px">
    <div class="brand-dot"></div>
    <div>
      <div class="brand-name">Brimvane.com</div>
      <div class="brand-sub">Marrowfen Fiber Optics</div>
    </div>
  </div>
  <div class="top-links abs"><span>USERS</span><span>|</span><span>SUPPORT</span></div>
  <div class="top-phone abs">
    <svg viewBox="0 0 24 24" width="16" height="16" fill="#fff"><path d="M6.6 10.8a15 15 0 006.6 6.6l2.2-2.2c.3-.3.7-.4 1-.2 1.1.4 2.3.6 3.6.6.6 0 1 .4 1 1V20c0 .6-.4 1-1 1A17 17 0 013 4c0-.6.4-1 1-1h3.5c.6 0 1 .4 1 1 0 1.3.2 2.5.6 3.6.1.3 0 .7-.2 1z"/></svg>
    1-888-555-0142
  </div>
  <div class="top-line abs"></div>
  <nav class="main-nav abs">
    <span>HOME</span><span>RESIDENTIAL</span><span>BUSINESS</span><span>SERVICES</span><span>FAQ</span><span>TELECOM</span><span>CONTACT US</span>
  </nav>
</header>

<!-- hero -->
<section class="hero abs" role="img" aria-label="Photo of two smiling women looking at a laptop on a sofa"></section>
<div class="band-edge" style="top:576px;background:var(--red)"></div>
<h1 class="hero-title abs">Marrowfen Fiber Optics</h1>
<p class="hero-sub abs">Service offers low cost, high quality, and extremely reliable phone, TV and high-speed internet access.</p>
<a class="btn hero-cta">GET IN TOUCH <svg viewBox="0 0 16 16"><circle cx="8" cy="8" r="8" fill="#fff"/><path d="M6.5 4.5L10 8l-3.5 3.5" stroke="#0a4aa8" stroke-width="2" fill="none"/></svg></a>
<div class="hero-badge abs"><i></i>I BEAMED UP WITH MARROWFEN</div>

<!-- about -->
<div class="photo-circle abs" style="left:140px;top:699px;width:406px;height:406px;background:radial-gradient(circle at 45% 50%,#9fe3ff 0%,#2f8fe0 30%,#0c3f8c 65%,#061a40 100%);box-shadow:0 10px 30px rgba(0,0,0,.2)" role="img" aria-label="Abstract image of glowing blue fiber optic light trails"></div>
<h2 class="heading about-title abs">About <span class="accent">Us</span></h2>
<div class="rule" style="left:616px;top:756px;width:208px"></div>
<div class="about-copy abs">
  <p>We are a 30 year old internet company who started as a dial up internet provider in our basement. Today we design, build, and maintain our own fiber optic internet network to provide service to residential, business, educational, healthcare, and governmental customers</p>
  <p>Lorem ipsum dolor sit amet, consectetur adipiscing elit, sed do eiusmod tempor incididunt ut labore et dolore magna aliqua. Ut enim ad minim veniam, quis nostrud exercitation ullamco laboris nisi ut aliquip ex ea commodo consequat. Duis aute irure dolor in reprehenderit in voluptate velit esse cillum dolore eu fugiat nulla pariatur.</p>
</div>
<a class="btn" style="left:619px;top:1054px;width:160px;height:42px">LEARN MORE <svg viewBox="0 0 16 16"><circle cx="8" cy="8" r="8" fill="#fff"/><path d="M6.5 4.5L10 8l-3.5 3.5" stroke="#0a4aa8" stroke-width="2" fill="none"/></svg></a>

<!-- pricing -->
<div class="pricing-band abs"></div>
<h2 class="heading section-title abs" style="top:1252px">Our <span class="accent">Pricing</span></h2>
<div class="rule" style="left:497px;top:1318px;width:206px"></div>

<div class="price-card card-dark abs" style="left:200px">
  <div class="name">VoIP<br>Phone Service</div><div class="bar"></div>
  <div class="amount">$25/<small> MONTH</small></div>
  <div class="desc">Marrowfen fiber optic service can save you money every month with reliable phone service. Keep your same number, FREE Voice Mail and Caller ID...</div>
</div>
<div class="price-card card-blue abs" style="left:470px">
  <div class="name">High Speed<br>Internet Service</div><div class="bar"></div>
  <div class="amount">$55/<small> MONTH</small></div>
  <div class="desc">Marrowfen fiber optic service bringsthe highest quality, fastest, and most reliable internet to your home 25mbps download starting at...</div>
</div>
<div class="price-card card-red abs" style="left:740px">
  <div class="name">Phone &amp;<br>Internet Packages</div><div class="bar"></div>
  <div class="amount">$80/<small> MONTH</small></div>
  <div class="desc">Save even more money by choosing Marrowfen for both your phone and internet service. starting at...</div>
</div>
<a class="btn buy" style="left:249px">BUY NOW <svg viewBox="0 0 16 16"><circle cx="8" cy="8" r="8" fill="#fff"/><path d="M6.5 4.5L10 8l-3.5 3.5" stroke="#d7141a" stroke-width="2" fill="none"/></svg></a>
<a class="btn buy" style="left:519px">BUY NOW <svg viewBox="0 0 16 16"><circle cx="8" cy="8" r="8" fill="#fff"/><path d="M6.5 4.5L10 8l-3.5 3.5" stroke="#d7141a" stroke-width="2" fill="none"/></svg></a>
<a class="btn buy" style="left:789px">BUY NOW <svg viewBox="0 0 16 16"><circle cx="8" cy="8" r="8" fill="#fff"/><path d="M6.5 4.5L10 8l-3.5 3.5" stroke="#d7141a" stroke-width="2" fill="none"/></svg></a>

<!-- services -->
<h2 class="heading section-title abs" style="top:1794px">Our <span class="accent">Services</span></h2>
<div class="rule" style="left:497px;top:1860px;width:206px"></div>
<div class="photo-circle abs" style="left:155px;top:1976px;width:410px;height:410px;background:linear-gradient(135deg,#ece6ee,#c9c5c8 55%,#8d8f95)" role="img" aria-label="Photo of a couple relaxing on a sofa using a tablet and phone"></div>
<svg class="abs" style="left:580px;top:1990px;width:120px;height:400px" viewBox="0 0 120 400"><path d="M30 30 Q60 60 90 85 Q120 140 100 190 Q90 250 75 295 Q40 340 35 390" stroke="#555" stroke-width="1.2" stroke-dasharray="3 3" fill="none"/></svg>

<div class="service abs" style="left:548px;top:1932px">
  <div class="service-icon blue"><svg viewBox="0 0 40 40" fill="none" stroke="#fff" stroke-width="2"><path d="M6 20 L20 8 L34 20"/><path d="M10 17 V33 H30 V17"/><rect x="17" y="23" width="6" height="10"/></svg></div>
  <div><h3 style="font-weight:700">RESIDENTIAL</h3><p>Identify and engage anonymous website visitors, converting them...</p></div>
</div>
<div class="service abs" style="left:633px;top:2037px">
  <div class="service-icon red"><svg viewBox="0 0 40 40" fill="none" stroke="#fff" stroke-width="2"><circle cx="20" cy="13" r="6"/><path d="M8 34 C8 24 32 24 32 34"/></svg></div>
  <div><h3>Buisness</h3><p>Connect with prospects seamlessly across social networks, Email, forums,....</p></div>
</div>
<div class="service abs" style="left:653px;top:2143px">
  <div class="service-icon blue"><svg viewBox="0 0 40 40" fill="none" stroke="#fff" stroke-width="2"><path d="M6 14 L20 6 L34 14 Z"/><path d="M10 16 V30 M16 16 V30 M24 16 V30 M30 16 V30 M6 33 H34"/></svg></div>
  <div><h3>governmental customers</h3><p>Stay ahead with real-time insights into customer sentiment and industry trends...</p></div>
</div>
<div class="service abs" style="left:624px;top:2246px">
  <div class="service-icon red"><svg viewBox="0 0 40 40" fill="none" stroke="#fff" stroke-width="2"><path d="M6 12 H18 Q20 12 20 15 V32 Q20 29 17 29 H6Z M34 12 H22 Q20 12 20 15 V32 Q20 29 23 29 H34Z"/></svg></div>
  <div><h3>Educational</h3><p>Stay ahead with real-time insights into customer sentiment and industry trends...</p></div>
</div>
<div class="service abs" style="left:557px;top:2351px">
  <div class="service-icon blue"><svg viewBox="0 0 40 40" fill="none" stroke="#fff" stroke-width="2"><path d="M17 12 H23 V17 H28 V23 H23 V28 H17 V23 H12 V17 H17Z"/><path d="M6 28 Q12 36 20 34"/></svg></div>
  <div><h3>Healthcare</h3><p>Experience precise insights and personalized communication tailored....</p></div>
</div>

<!-- experience -->
<section class="experience abs"></section>
<div class="band-edge" style="top:2530px;background:var(--line-soft)"></div>
<h2 class="exp-title abs"><b>Experience</b> the Difference</h2>
<div class="rule" style="left:497px;top:2662px;width:206px;background:var(--white)"></div>
<p class="exp-copy abs">Marrowfen outperforms other local Internet and phone service providers by delivering Internet and phone service over the newest, most reliable communications network - Fiber Optics!<br>Utilizing our own fiber optic network, we can bring you internet speeds that far surpass traditional DSL or Cable services. Internet service that is consistent and reliable, combined with superior phone voice quality, makes Marrowfen Fiber Optic the perfect choice for home and business.</p>
<div class="feature abs" style="left:207px;top:2818px">
  <svg viewBox="0 0 90 90" fill="none" stroke="#fff" stroke-width="3"><circle cx="45" cy="38" r="26"/><circle cx="45" cy="32" r="8"/><path d="M31 52 Q45 38 59 52"/><path d="M12 78 H40 L60 66"/></svg>
  LOCAL SUPPORT
</div>
<div class="feature abs" style="left:468px;top:2818px">
  <svg viewBox="0 0 90 90" fill="none" stroke="#fff" stroke-width="3"><circle cx="50" cy="38" r="16"/><path d="M55 31 Q50 27 45 31 Q45 38 50 38 Q55 38 55 45 Q50 49 45 45 M50 26 V50"/><path d="M50 6 V14 M40 8 V14 M60 8 V14"/><path d="M10 78 H38 L72 64"/></svg>
  SAVE MONEY
</div>
<div class="feature abs" style="left:730px;top:2818px">
  <svg viewBox="0 0 90 90" fill="none" stroke="#fff" stroke-width="3"><path d="M78 10 Q50 12 34 40 L48 54 Q76 38 78 10Z"/><circle cx="56" cy="32" r="6"/><path d="M34 40 L20 40 L30 28 M48 54 L48 68 L60 58 M30 60 L16 74"/></svg>
  GETTING STARTED
</div>

<!-- service area -->
<div class="map abs" role="img" aria-label="Map of the western Pennsylvania service region"></div>
<div class="area-card abs"></div>
<h2 class="heading area-title abs">Service <span class="accent">Area</span></h2>
<div class="rule" style="left:650px;top:3191px;width:160px"></div>
<p class="area-list abs"><span class="first">Altoona</span>, Apollo, Blairsville, Brackenridge, Clymer, Creighton, Dayton, Elderton, Ford City, Freeport, Homer City, Indiana, Kittanning, Leechburgh, Natrona Heights, New Bethlehem, New Kensington, Rural Valley, Saltsburg, Sarver, Springdale, Tarentum, and Worthington</p>
<div class="call-label abs">PLEASE GIVE US A CALL AT</div>
<div class="call-nums abs">724-555-0186 / 1-888-555-0142</div>
<a class="btn" style="left:619px;top:3459px;width:160px;height:42px">CONTACT US <svg viewBox="0 0 16 16"><circle cx="8" cy="8" r="8" fill="#fff"/><path d="M6.5 4.5L10 8l-3.5 3.5" stroke="#0a4aa8" stroke-width="2" fill="none"/></svg></a>

<!-- footer -->
<footer class="site-footer abs"></footer>
<div class="brand abs" style="left:126px;top:3684px">
  <div class="brand-dot"></div>
  <div>
    <div class="brand-name" style="color:#fff">Brimvane.com</div>
    <div class="brand-sub" style="color:#fff">Marrowfen Fiber Optics</div>
  </div>
</div>
<nav class="footer-nav abs" style="color:#fff">
  <span>HOME</span><span>RESIDENTIAL</span><span>BUSINESS</span><span>SERVICES</span><span>FAQ</span><span>TELECOM</span><span>CONTACT US</span>
</nav>
<div class="footer-col abs" style="left:125px;color:#fff"><h4>Location</h4>Marrowfen Inc. 118 Harbor Lane,<br>Millbrook, PA 10000</div>
<div class="footer-col abs" style="left:393px;color:#fff"><h4>Phone</h4>724-555-0186<br>Toll Free: 1-888-555-0142</div>
<div class="footer-col abs" style="left:662px;color:#fff"><h4>Email</h4>Sales: sales@brimvane.com<br>Support: support@brimvane.com</div>
<div class="footer-col abs" style="left:930px;color:#fff"><h4>Office Hours</h4>Sunday: &nbsp;&nbsp;4pm - 8pm<br>Mon to Fri; &nbsp;&nbsp;8am - 6pm<br>Saturday: 12pm - 4pm</div>
<div class="footer-rule abs"></div>
<div class="copyright abs" style="color:#fff">Copyright@2024 - All Rights Reserved</div>

</body>
</html>
```